Zielgruppe
Wir sind eine Wäscherei.
Zielgruppe: Kunden aus der Hotel- und Gastronomiebranche
Aufgabenstellung
Wir benötigen einen 2-seitigen Flyer DIN lang. 9,8 x21cm
TextInhalte sind in der Vorlage-Datei.
Bilder sind eingefügt.

```html
<!DOCTYPE html>
<html lang="de">
<head>
<meta charset="utf-8">
<title>Wäscherei Kelbring – Flyer</title>
<link href="https://fonts.googleapis.com/css2?family=Nunito+Sans:wght@400;700;800&display=swap" rel="stylesheet">
<style>
  :root {
    --magenta: #c2006f;
    --ink: #111111;
    --paper: #ffffff;
    --photo-light: #eef0f2;
    --photo-mid: #d9dcdf;
    --photo-warm: #c9b8a6;
    --photo-dark: #3a2a22;
  }
  * { margin: 0; padding: 0; box-sizing: border-box; }
  html, body { width: 1200px; height: 560px; overflow: hidden; background: var(--paper); }
  body { font-family: "Nunito Sans", Arial, sans-serif; color: var(--ink); }

  .flyer { position: relative; width: 1200px; height: 560px; background: var(--paper); }

  .brand {
    position: absolute; left: 57px; top: 146px;
    display: flex; align-items: center; gap: 12px;
  }
  .brand-mark { width: 18px; height: 18px; background: var(--magenta); }
  .brand-name {
    font-weight: 800; font-size: 38px; letter-spacing: 0.5px;
    color: var(--magenta); text-transform: uppercase; line-height: 1;
  }

  .services { position: absolute; left: 57px; top: 247px; }
  .services-lead { font-weight: 700; font-size: 18.5px; color: var(--magenta); margin-bottom: 2px; }
  .service-list { list-style: none; }
  .service-list li {
    font-size: 18.5px; line-height: 24.2px; padding-left: 10px; position: relative;
  }
  .service-list li::before {
    content: ""; position: absolute; left: 1px; top: 11px;
    width: 4px; height: 4px; background: var(--magenta); transform: rotate(45deg);
  }

  .contact {
    position: absolute; left: 57px; top: 490px;
    display: flex; align-items: center; font-size: 12.5px; white-space: nowrap;
  }
  .contact .sep {
    display: inline-block; width: 4px; height: 4px; margin: 0 5px;
    background: var(--magenta); transform: rotate(45deg);
  }
  .contact .icon { width: 11px; height: 11px; margin: 0 5px 0 8px; fill: var(--magenta); }

  .photo { position: absolute; }
  .photo-banquet { left: 808px; top: 0; width: 392px; height: 181px;
    background: linear-gradient(160deg, var(--photo-mid), var(--photo-light) 55%, #c8cfc4); }
  .photo-fan { left: 808px; top: 191px; width: 190px; height: 177px;
    background: linear-gradient(135deg, var(--photo-warm), var(--photo-light) 60%, #e4e0da); }
  .photo-cone { left: 1010px; top: 191px; width: 190px; height: 177px;
    background: linear-gradient(120deg, var(--photo-dark), #6b4634 45%, var(--photo-light) 80%); }
  .photo-glasses { left: 808px; top: 377px; width: 190px; height: 183px;
    background: linear-gradient(170deg, #b9b1a4, var(--photo-light) 60%, #cfcbc5); }
  .photo-fold { left: 1010px; top: 377px; width: 190px; height: 183px;
    background: linear-gradient(150deg, #f6f6f6, var(--photo-mid) 70%, #c6c8ca); }
</style>
</head>
<body>
<main class="flyer">
  <div class="brand">
    <span class="brand-mark"></span>
    <span class="brand-name">Wäscherei Kelbring</span>
  </div>

  <section class="services">
    <p class="services-lead">Serviettenfaltservice – ab November 2017</p>
    <ul class="service-list">
      <li>Hotel- und Gastronomiewäsche</li>
      <li>Schmutzmatten</li>
      <li>Gardinenservice</li>
      <li>Berufskleidung</li>
      <li>Private Wäsche</li>
      <li>Verkauf von Hotel- und Gastronomietextilien</li>
    </ul>
  </section>

  <footer class="contact">
    <span>Wäscherei Kelbring</span><span class="sep"></span>
    <span>Lindenweg 14</span><span class="sep"></span>
    <span>70999 Talhausen</span>
    <svg class="icon" viewBox="0 0 24 24" aria-hidden="true"><path d="M6.6 10.8a15 15 0 0 0 6.6 6.6l2.2-2.2a1 1 0 0 1 1-.25 11.4 11.4 0 0 0 3.6.57 1 1 0 0 1 1 1V20a1 1 0 0 1-1 1A17 17 0 0 1 3 4a1 1 0 0 1 1-1h3.5a1 1 0 0 1 1 1c0 1.25.2 2.45.57 3.57a1 1 0 0 1-.25 1z"/></svg>
    <span>+49 (0) 7000 / 12 34 50</span>
    <svg class="icon" viewBox="0 0 24 24" aria-hidden="true"><path d="M2 5h20v14H2zm2 2v.5l8 5 8-5V7zm0 2.8V17h16V9.8l-8 5z"/></svg>
    <span>info@waescherei-kelbring.de</span>
  </footer>

  <div class="photo photo-banquet" role="img" aria-label="Festlich gedeckte Tafel mit weißen Tischdecken, Gläsern und Blumengesteck"></div>
  <div class="photo photo-fan" role="img" aria-label="Weiße Serviette als Fächer gefaltet"></div>
  <div class="photo photo-cone" role="img" aria-label="Spitz gefaltete weiße Serviette zwischen Weingläsern"></div>
  <div class="photo photo-glasses" role="img" aria-label="Gedeckter Platz mit Gläsern und Serviette auf Platzteller"></div>
  <div class="photo photo-fold" role="img" aria-label="Kunstvoll gefaltete weiße Serviette auf einem Teller"></div>
</main>
</body>
</html>
```